I am a highly experienced private practice psychotherapist serving high end clientele in the Wall Street area of New York City. I need electronic letterhead (that can also be printed) to use for bills, receipts, and correspondences.

My clients are very high end and are used to elegance and wealth. The letterhead should contain the following information: Marissa K. Tolland, LCSW 57 Pinegate Avenue, Suite 2716 New York, NY 10392 Phone : (917) 555-3179 email: therapy@marissatollandlcsw.example website: www.marissatollandlcsw.example

Thank you for your designs. Please be advised that the letterhead will be used for bills/invoices; professional letters to other mental health professionals and doctors, as well as to attorneys. It needs to be highly professional in the same way that a law firm has professional and elegant letterhead, raher than whimsical or with spa designers. My letters end up as official documents.

```html
<!DOCTYPE html>
<html lang="en">
<head>
<meta charset="utf-8">
<title>Marissa K. Tolland, LCSW — Letterhead</title>
<link rel="stylesheet" href="https://fonts.googleapis.com/css2?family=PT+Sans:wght@400;700&family=PT+Sans+Narrow:wght@400;700&display=swap">
<style>
  :root {
    --backdrop: #1a1613;
    --paper: #f7f7f7;
    --ink: #3b3b3b;
    --ink-soft: #6a6a6a;
    --rule: #3d3d3d;
    --plum: #93278f;
    --crimson: #a91d24;
    --white: #ffffff;
  }
  * { margin: 0; padding: 0; box-sizing: border-box; }
  html, body {
    width: 1200px; height: 837px; overflow: hidden;
    background: var(--backdrop);
  }
  .stage { position: relative; width: 1200px; height: 837px; }

  .letterhead {
    position: absolute; top: 18px;
    width: 570px; height: 805px;
    background: var(--paper);
    overflow: hidden;
  }
  .letterhead--plum { left: 20px; --accent: var(--plum); }
  .letterhead--crimson { left: 616px; --accent: var(--crimson); }

  .accent-band {
    position: absolute; left: 0; top: 0;
    width: 94px; height: 100%;
    background: var(--accent);
  }

  .footer-rule {
    position: absolute; top: 716px; left: 56px;
    width: 465px; height: 3px;
    background: linear-gradient(to right, var(--white) 0 38px, var(--rule) 38px);
  }

  .practitioner-name {
    position: absolute; top: 726px; left: 100px;
    font-family: "PT Sans Narrow", sans-serif;
    font-weight: 700; font-size: 9px;
    letter-spacing: 2.2px; text-transform: uppercase;
    color: var(--ink);
  }

  .contact-list { list-style: none; }
  .contact-item {
    position: absolute; left: 0; height: 11px;
    display: flex; align-items: center;
  }
  .contact-item svg {
    position: absolute; left: 80px; width: 8px; height: 8px;
    fill: var(--white);
  }
  .contact-text {
    position: absolute; left: 98px; white-space: nowrap;
    font-family: "PT Sans", sans-serif; font-size: 9px;
    color: var(--ink); line-height: 11px;
  }
  .contact-item--phone { top: 746px; }
  .contact-item--email { top: 757px; }
  .contact-item--web { top: 769px; }
  .contact-item--address { top: 780px; }
  .contact-item--phone .contact-text,
  .contact-item--web .contact-text { font-weight: 700; }
  .contact-item--address .contact-text {
    font-family: "PT Sans Narrow", sans-serif;
    font-size: 8px; color: var(--ink-soft);
  }
</style>
</head>
<body>
<div class="stage">

  <section class="letterhead letterhead--plum">
    <div class="accent-band"></div>
    <div class="footer-rule"></div>
    <p class="practitioner-name">Marissa K. Tolland, LCSW</p>
    <ul class="contact-list">
      <li class="contact-item contact-item--phone">
        <svg viewBox="0 0 10 10" aria-hidden="true"><path d="M2 0.5 L3.6 2.6 L2.8 3.6 Q4 6 6.4 7.2 L7.4 6.4 L9.5 8 L8.4 9.5 Q4.5 9.2 1.8 6.4 Q0.3 4 0.5 1.6 Z"/></svg>
        <span class="contact-text">(917) 555-3179</span>
      </li>
      <li class="contact-item contact-item--email">
        <svg viewBox="0 0 10 10" aria-hidden="true"><path d="M0.5 2.5 H9.5 V8 H0.5 Z"/><path d="M0.5 2.5 L5 5.8 L9.5 2.5" stroke="#93278f" stroke-width="0.8" fill="none"/></svg>
        <span class="contact-text">therapy@marissatollandlcsw.example</span>
      </li>
      <li class="contact-item contact-item--web">
        <svg viewBox="0 0 10 10" aria-hidden="true"><circle cx="5" cy="5" r="4.5"/><path d="M2.5 3 Q4 4 3.5 5.5 M6 2 Q7.5 4 6.5 7" stroke="#93278f" stroke-width="1" fill="none"/></svg>
        <span class="contact-text">www.marissatollandlcsw.example</span>
      </li>
      <li class="contact-item contact-item--address">
        <svg viewBox="0 0 10 10" aria-hidden="true"><path d="M0.5 4 L5 0.8 L9.5 4 V9.2 H0.5 Z"/><path d="M0.5 4 L5 7 L9.5 4" stroke="#93278f" stroke-width="0.8" fill="none"/></svg>
        <span class="contact-text">57 Pinegate Avenue, Suite 2716 New York, NY 10392</span>
      </li>
    </ul>
  </section>

  <section class="letterhead letterhead--crimson">
    <div class="accent-band"></div>
    <div class="footer-rule"></div>
    <p class="practitioner-name">Marissa K. Tolland, LCSW</p>
    <ul class="contact-list">
      <li class="contact-item contact-item--phone">
        <svg viewBox="0 0 10 10" aria-hidden="true"><path d="M2 0.5 L3.6 2.6 L2.8 3.6 Q4 6 6.4 7.2 L7.4 6.4 L9.5 8 L8.4 9.5 Q4.5 9.2 1.8 6.4 Q0.3 4 0.5 1.6 Z"/></svg>
        <span class="contact-text">(917) 555-3179</span>
      </li>
      <li class="contact-item contact-item--email">
        <svg viewBox="0 0 10 10" aria-hidden="true"><path d="M0.5 2.5 H9.5 V8 H0.5 Z"/><path d="M0.5 2.5 L5 5.8 L9.5 2.5" stroke="#a91d24" stroke-width="0.8" fill="none"/></svg>
        <span class="contact-text">therapy@marissatollandlcsw.example</span>
      </li>
      <li class="contact-item contact-item--web">
        <svg viewBox="0 0 10 10" aria-hidden="true"><circle cx="5" cy="5" r="4.5"/><path d="M2.5 3 Q4 4 3.5 5.5 M6 2 Q7.5 4 6.5 7" stroke="#a91d24" stroke-width="1" fill="none"/></svg>
        <span class="contact-text">www.marissatollandlcsw.example</span>
      </li>
      <li class="contact-item contact-item--address">
        <svg viewBox="0 0 10 10" aria-hidden="true"><path d="M0.5 4 L5 0.8 L9.5 4 V9.2 H0.5 Z"/><path d="M0.5 4 L5 7 L9.5 4" stroke="#a91d24" stroke-width="0.8" fill="none"/></svg>
        <span class="contact-text">57 Pinegate Avenue, Suite 2716 New York, NY 10392</span>
      </li>
    </ul>
  </section>

</div>
</body>
</html>
```